Brightwave Business Card

Professional Business Card Design required using the attached contact information.

Contact information can be rearranged as required.

The company is a new start up venture developing solar systems, the branding should be in keeping with that of one of the investors whose website is as follows https://www.quorvex.com/

```html
<!DOCTYPE html>
<html lang="en">
<head>
<meta charset="utf-8">
<title>Brightwave Renewables – Business Card</title>
<link href="https://fonts.googleapis.com/css2?family=Montserrat:wght@400;600;700&display=swap" rel="stylesheet">
<style>
  :root {
    --backdrop: #e9e9e7;
    --card: #fbfbfa;
    --ink: #1b1b1b;
    --green: #1f6a4e;
    --grey: #555a57;
  }
  * { margin: 0; padding: 0; box-sizing: border-box; }
  html, body {
    width: 1200px; height: 800px; overflow: hidden;
    background: var(--backdrop);
    font-family: "Montserrat", Arial, sans-serif;
  }
  .card {
    position: absolute; left: 110px; top: 120px;
    width: 980px; height: 560px;
    background: var(--card);
    box-shadow: 0 6px 24px rgba(0,0,0,0.12);
  }
  .wordmark {
    position: absolute; right: 70px; top: 96px;
    display: flex; align-items: center; gap: 20px;
  }
  .wordmark-dot {
    width: 18px; height: 18px; border-radius: 50%;
    background: var(--green);
  }
  .wordmark-name {
    font-weight: 600; font-size: 44px; letter-spacing: 4px;
    color: var(--ink); text-transform: uppercase;
  }
  .details {
    position: absolute; left: 110px; top: 270px;
  }
  .person-name {
    font-weight: 700; font-size: 40px; color: var(--green);
    letter-spacing: 0.5px; margin-bottom: 22px;
  }
  .company {
    font-weight: 700; font-size: 24px; color: var(--green);
    letter-spacing: 0.5px;
  }
  .address {
    font-weight: 400; font-size: 25px; color: var(--grey);
    letter-spacing: 1px; margin-bottom: 16px;
  }
  .contact-list { list-style: none; }
  .contact-list li {
    display: flex; align-items: center; gap: 12px;
    font-size: 25px; color: var(--grey); letter-spacing: 1px;
    line-height: 34px;
  }
  .contact-icon { width: 18px; height: 18px; flex: none; fill: var(--green); }
</style>
</head>
<body>
  <section class="card">
    <div class="wordmark">
      <span class="wordmark-dot"></span>
      <span class="wordmark-name">Brightwave Renewables</span>
    </div>

    <div class="details">
      <h1 class="person-name">Daniel Hartwell</h1>
      <p class="company">Brightwave Renewables LLC</p>
      <p class="address">218 Harbor Street, Boston, MA 02110</p>
      <ul class="contact-list">
        <li>
          <svg class="contact-icon" viewBox="0 0 24 24" aria-hidden="true"><path d="M6.6 10.8a15.1 15.1 0 0 0 6.6 6.6l2.2-2.2c.3-.3.7-.4 1-.2 1.1.4 2.3.6 3.6.6.6 0 1 .4 1 1V20c0 .6-.4 1-1 1A17 17 0 0 1 3 4c0-.6.4-1 1-1h3.5c.6 0 1 .4 1 1 0 1.3.2 2.5.6 3.6.1.3 0 .7-.2 1z"/></svg>
          +1 (555) 014-2276
        </li>
        <li>
          <svg class="contact-icon" viewBox="0 0 24 24" aria-hidden="true"><path d="M2 5h20v14H2z M3 6l9 7 9-7" /><path d="M2 5l10 8 10-8v1l-10 8L2 6z" fill="#fbfbfa"/></svg>
          daniel.hartwell@brightwave-renewables.com
        </li>
        <li>
          <svg class="contact-icon" viewBox="0 0 24 24" aria-hidden="true"><circle cx="12" cy="12" r="10"/><path d="M2 12h20M12 2c3 3 3 17 0 20M12 2c-3 3-3 17 0 20" stroke="#fbfbfa" stroke-width="1.5" fill="none"/></svg>
          www.brightwave-renewables.com
        </li>
      </ul>
    </div>
  </section>
</body>
</html>
```